Bramwell Business Cards

Logo files are included. Full "Bramwell" logo should be included on the back of the business card. The B symbol should be included on the front with the contact information.

Bramwell, LLC is the company name and we do commercial construction and real estate development consulting services. Look for a fairly simple card design utilizing our logo.

```html
<!DOCTYPE html>
<html lang="en">
<head>
<meta charset="utf-8">
<title>Bramwell Business Cards</title>
<link rel="stylesheet" href="https://fonts.googleapis.com/css2?family=Montserrat:wght@400;600;700&display=swap">
<style>
  :root {
    --navy: #1b374c;
    --gold: #ebac0a;
    --paper: #ffffff;
    --ink-soft: #8a8f94;
    --backdrop: #2b2b2d;
  }
  * { margin: 0; padding: 0; box-sizing: border-box; }
  html, body {
    width: 1200px; height: 1024px; overflow: hidden;
    background: var(--backdrop);
    font-family: "Montserrat", Arial, sans-serif;
  }
  .card {
    position: absolute; left: 300px;
    width: 600px; height: 343px;
    background: var(--paper);
    overflow: hidden;
    box-shadow: 0 10px 30px rgba(0,0,0,.45);
  }
  .card--back { top: 110px; }
  .card--front { top: 540px; }

  /* back */
  .back-logo {
    position: absolute; left: 0; right: 0; top: 120px;
    display: flex; align-items: center; justify-content: center; gap: 18px;
  }
  .logo-dot {
    width: 54px; height: 54px; border-radius: 50%;
    border: 6px solid var(--navy);
  }
  .wordmark {
    font-weight: 600; color: var(--navy);
    letter-spacing: 3px; text-transform: uppercase;
  }
  .back-logo .wordmark { font-size: 46px; }
  .back-bands { position: absolute; left: 0; bottom: 0; width: 600px; height: 24px; }

  /* front */
  .card--front .wordmark { position: absolute; left: 70px; top: 72px; font-size: 34px; }
  .person { position: absolute; right: 46px; top: 34px; text-align: right; }
  .person-name { font-size: 22px; font-weight: 700; letter-spacing: 1px; color: var(--navy); }
  .person-name .surname { color: var(--gold); }
  .person-role { font-size: 13px; color: var(--ink-soft); margin-top: 2px; }
  .contact {
    position: absolute; left: 70px; bottom: 34px;
    font-size: 13px; color: var(--ink-soft); line-height: 1.45;
    list-style: none;
  }
  .contact-address { margin-bottom: 8px; }
  .contact li { display: flex; align-items: center; gap: 8px; }
  .contact-icon { width: 14px; height: 14px; flex: none; }
  .front-ring { position: absolute; right: 0; bottom: 0; }
</style>
</head>
<body>

<section class="card card--back">
  <div class="back-logo">
    <span class="logo-dot"></span>
    <span class="wordmark">Bramwell</span>
  </div>
  <svg class="back-bands" viewBox="0 0 600 24" aria-hidden="true">
    <polygon points="0,12 385,12 398,24 0,24" fill="var(--navy)"/>
    <polygon points="400,0 600,0 600,14 410,14" fill="var(--gold)"/>
  </svg>
</section>

<section class="card card--front">
  <div class="wordmark">Bramwell</div>

  <div class="person">
    <div class="person-name">CLARA <span class="surname">HENSLEY</span></div>
    <div class="person-role">CEO/Owner</div>
  </div>

  <ul class="contact">
    <li class="contact-address">48 Harlow Street, Eastbrook,<br>ME 04021</li>
    <li>
      <svg class="contact-icon" viewBox="0 0 14 14" aria-hidden="true"><circle cx="7" cy="7" r="7" fill="var(--gold)"/><path d="M4.5 3.8l1.4-.3.7 1.6-.8.6c.4.9 1 1.5 1.9 1.9l.6-.8 1.6.7-.3 1.4c-2.8 0-5.1-2.3-5.1-5.1z" fill="#fff"/></svg>
      (555) 014-2290
    </li>
    <li>
      <svg class="contact-icon" viewBox="0 0 14 14" aria-hidden="true"><circle cx="7" cy="7" r="7" fill="var(--gold)"/><rect x="3.5" y="4.5" width="7" height="5" fill="#fff"/><path d="M3.5 4.5L7 7.3l3.5-2.8" stroke="var(--gold)" stroke-width=".8" fill="none"/></svg>
      info@bramwellllc.com
    </li>
    <li>
      <svg class="contact-icon" viewBox="0 0 14 14" aria-hidden="true"><circle cx="7" cy="7" r="7" fill="var(--gold)"/><circle cx="7" cy="7" r="3.6" stroke="#fff" stroke-width=".9" fill="none"/><path d="M3.4 7h7.2M7 3.4c-1.6 2-1.6 5.2 0 7.2M7 3.4c1.6 2 1.6 5.2 0 7.2" stroke="#fff" stroke-width=".8" fill="none"/></svg>
      www.bramwellllc.com
    </li>
  </ul>

  <svg class="front-ring" width="240" height="250" viewBox="0 0 240 250" aria-hidden="true">
    <circle cx="170" cy="175" r="135" fill="none" stroke="var(--navy)" stroke-width="12"/>
  </svg>
</section>

</body>
</html>
```